electric fence manufacturer needs a international catalogue

our company "vardane technology co.,ltd" is base on shenzhen China.
our product is electric fence system. including the energiser and accesories.
our system seperated into 2 section.
1.perimeter security product, pls check attachment for the project picture. we use the high voltage pulse to stop the intruder and bad man. once we touch the wire , you will get shock. but it is safe, just make you unconfortable.
2.farm electric fencing. to keep the animal inside or outside. the same function with security system.
we prefer color such as green. orange.
we want to express is our life is getting peace and comfortable and relax and easy by using electric fencing
3. page size A4

Target Market(s)

global market ,

Industry/Entity Type

Security

```html
<!DOCTYPE html>
<html lang="en">
<head>
<meta charset="utf-8">
<title>About Us | Vardane Technology</title>
<link rel="stylesheet" href="https://fonts.googleapis.com/css2?family=Arimo:wght@400;700&family=Montserrat:wght@400&display=swap">
<style>
  :root {
    --orange: #f5873a;
    --ink: #1a1a1a;
    --white: #ffffff;
    --black: #000000;
    --sky: #a9c2dc;
    --sky-light: #c9d8e6;
    --wall: #e2e2df;
    --wall-shade: #bdbdb9;
    --fence-dark: #4a4a48;
  }
  html, body {
    margin: 0;
    padding: 0;
    overflow: hidden;
    background: var(--white);
  }
  .page {
    position: relative;
    width: 849px;
    height: 1200px;
    overflow: hidden;
    background: var(--white);
    font-family: "Arimo", Arial, sans-serif;
  }
  .site-photo {
    position: absolute;
    left: 0;
    top: 340px;
    width: 849px;
    height: 780px;
    background:
      radial-gradient(ellipse 260px 420px at 470px 620px, rgba(74,74,72,0.55), rgba(74,74,72,0) 100%),
      radial-gradient(ellipse 200px 300px at 760px 700px, rgba(90,90,88,0.45), rgba(90,90,88,0) 100%),
      linear-gradient(90deg, var(--sky) 0%, var(--sky-light) 32%, var(--wall) 44%, var(--white) 62%, var(--wall-shade) 100%);
    -webkit-mask-image: linear-gradient(180deg, transparent 0%, #000 26%);
    mask-image: linear-gradient(180deg, transparent 0%, #000 26%);
  }
  .title-bar {
    position: absolute;
    left: 0;
    top: 40px;
    width: 376px;
    height: 47px;
    background: var(--orange);
  }
  .title-bar h1 {
    margin: 0;
    padding-left: 40px;
    font-family: "Montserrat", sans-serif;
    font-weight: 400;
    font-size: 33px;
    line-height: 50px;
    color: var(--white);
    letter-spacing: 0.5px;
  }
  .about-text {
    position: absolute;
    left: 41px;
    top: 119px;
    width: 790px;
    color: var(--ink);
    font-size: 16.4px;
    line-height: 19px;
    white-space: nowrap;
  }
  .about-text p {
    margin: 0 0 19px 0;
  }
  .footer-wave {
    position: absolute;
    left: 0;
    top: 0;
    width: 849px;
    height: 1200px;
  }
  .footer-url {
    position: absolute;
    left: 41px;
    top: 1143px;
    color: var(--white);
    font-weight: 700;
    font-size: 13px;
  }
  .page-number {
    position: absolute;
    right: 41px;
    top: 1139px;
    color: var(--white);
    font-size: 17px;
  }
  .page-number strong { font-weight: 700; }
</style>
</head>
<body>
<div class="page">
  <div class="site-photo" role="img" aria-label="Photo of a building wall topped with an electric security fence, black posts and insulators with a yellow warning sign against a pale sky"></div>

  <div class="title-bar"><h1>About Us</h1></div>

  <div class="about-text">
    <p>Shenzhen Vardane Technology Co.,Ltd is established since 2007,dedicating to provide stable<br>professional products,solutions and services of electric fence, Vardane has offered perimeter security<br>service and agricultural livestock solutions of electric fence to thousands of companies and<br>governments in more than 20 provinces in China domestic market and foreign countries over 6 years.</p>
    <p>Best practised R&amp;D team and global management guarabtees the world-class technology and<br>industry-leading potential,our products are distributed to more than 40 countries worldwide. We are a<br>reliable electric fencing system for security and livestock supplier,facotry in China and abroad.</p>
    <p>Our products are approved by ISO 9001, CMA by china security department and CE certificate.<br>VD-polar serials are designed to meet the needs of all animal management protection and rotational<br>crop grazing requirement and pasture management,which can be integrated into solar power system.<br>and thery are in accordance with IEC 60335-2-76 and in conformance with AS/NZS CISPR14-1.<br>VD-2008 series is in accordance with IEC 60335-2-76 Moreover, water-proof box, connecting the wire<br>at the bottom, advanced high/low voltage mode and unique LCD display earns a outstanding<br>advantage in the market.</p>
    <p>To meet different customer's need, we design perimeter solution according to practical situation.<br>So far, these solutions are widely used in community, residential area, government, school, plants,<br>garage, prison, military bases, water and gas distributor, farmland and poultry area. We do offer<br>OEM/ODM service for energizer or accessories.</p>
  </div>

  <svg class="footer-wave" viewBox="0 0 849 1200" aria-hidden="true">
    <defs>
      <linearGradient id="goldBand" x1="0" y1="0" x2="1" y2="0">
        <stop offset="0" stop-color="#b98f45"/>
        <stop offset="0.35" stop-color="#e8c98a"/>
        <stop offset="0.7" stop-color="#f6e3b0"/>
        <stop offset="1" stop-color="#d8b26a"/>
      </linearGradient>
    </defs>
    <path d="M0,838 C160,850 300,955 450,1030 C560,1082 690,1098 849,1040 L849,1080 C690,1125 560,1112 450,1062 C300,992 150,885 0,878 Z" fill="url(#goldBand)"/>
    <path d="M0,878 C150,885 300,992 450,1062 C560,1112 690,1125 849,1080 L849,1200 L0,1200 Z" fill="#000"/>
  </svg>

  <div class="footer-url">www.vardanetech.com</div>
  <div class="page-number"><strong>1</strong> | Page</div>
</div>
</body>
</html>
```